Walt's 85th Birthday Invitation

Invitation to celebrate Walt's turning 85. OKTOBERFEST with fall colors & maybe some beer steins/autumn leaves/happy/fun images. Below are my thoughts for the wording but I need someone to bring it to life.
It's not just a party
it's an
OKTOBERFEST
to celebrate
Picture of Walt
Walt's 85th birthday

Saturday, October 25, 2014

at the Thornwick Ale Yard
Pellorwood
4172 Dunmere Ave.
Hollin Vale, CA 93617

Cocktails at 6 Dinner at 7
Dancing & Partying till 10:00

No birthday gifts please.
Please consider a gift to PellorWood!
Casual Attire

I would like this on a horizontal 5x7 flat card that will fit the envelopes you have. The text & spacing can be adjusted. This is just a rough draft. Thank you for your help! I will need 150 invitations with envelopes.

OktoberFest

```html
<!DOCTYPE html>
<html lang="en">
<head>
<meta charset="utf-8">
<title>Walt's 85th Birthday Oktoberfest Invitation</title>
<link rel="stylesheet" href="https://fonts.googleapis.com/css2?family=Bebas+Neue&family=UnifrakturCook:wght@700&family=Josefin+Sans:wght@300&display=swap">
<style>
  :root {
    --ink: #111111;
    --red: #c4202f;
    --red-soft: #d65a5a;
    --bg-olive: #a6a86b;
    --bg-sand: #c9ad6c;
    --bg-orange: #e89a5f;
    --bg-gold: #e9b85e;
  }
  html, body { margin: 0; padding: 0; overflow: hidden; }
  body { width: 1200px; height: 857px; }
  .invitation {
    position: relative;
    width: 1200px;
    height: 857px;
    overflow: hidden;
    background:
      radial-gradient(ellipse at 100% 0%, var(--bg-gold) 0%, rgba(233,184,94,0) 45%),
      linear-gradient(200deg, var(--bg-orange) 0%, var(--bg-sand) 45%, var(--bg-olive) 80%, #93a069 100%);
    font-family: 'Bebas Neue', 'Arial Narrow', sans-serif;
    color: var(--ink);
  }
  .art-slot {
    position: absolute;
    background: linear-gradient(180deg, var(--red-soft) 0%, var(--red) 100%);
    opacity: 0.85;
  }
  .art-slot--steins { top: 23px; width: 152px; height: 102px; }
  .art-slot--hats { top: 734px; width: 120px; height: 110px; }
  .rule {
    position: absolute;
    left: 57px;
    width: 1086px;
    height: 2px;
    background: var(--ink);
  }
  .rule--top { top: 138px; }
  .rule--bottom { top: 719px; }
  .photo-frame {
    position: absolute;
    left: 57px;
    top: 240px;
    width: 250px;
    height: 337px;
    border: 4px solid var(--ink);
  }
  .lead {
    position: absolute;
    left: 372px;
    top: 183px;
    margin: 0;
    font-size: 27px;
    line-height: 1;
    letter-spacing: 4.2px;
    text-transform: uppercase;
    white-space: nowrap;
  }
  .event-name {
    position: absolute;
    left: 381px;
    top: 236px;
    width: 440px;
    margin: 0;
    text-align: center;
    font-family: 'UnifrakturCook', 'Times New Roman', serif;
    font-weight: 700;
    font-size: 96px;
    line-height: 1.2;
    color: var(--red);
    -webkit-text-stroke: 1.5px #3a0d10;
    letter-spacing: 1px;
  }
  .celebrate {
    position: absolute;
    left: 415px;
    top: 394px;
    width: 372px;
    display: flex;
    align-items: center;
    gap: 8px;
    font-size: 27px;
    line-height: 1;
    letter-spacing: 3.5px;
    white-space: nowrap;
  }
  .celebrate .bars {
    flex: 1;
    height: 10px;
    border-top: 2px solid var(--ink);
    border-bottom: 2px solid var(--ink);
    position: relative;
  }
  .celebrate .bars::after {
    content: "";
    position: absolute;
    left: 0; right: 0; top: 2px;
    height: 2px;
    background: var(--ink);
  }
  .honoree {
    position: absolute;
    left: 353px;
    top: 452px;
    width: 490px;
    margin: 0;
    text-align: center;
    font-weight: 400;
    font-size: 50px;
    letter-spacing: 6px;
    line-height: 1;
    color: var(--red);
    -webkit-text-stroke: 1px #3a0d10;
    text-transform: uppercase;
    white-space: nowrap;
  }
  .honoree small { font-size: 30px; letter-spacing: 2px; }
  .date {
    position: absolute;
    left: 406px;
    top: 544px;
    width: 388px;
    height: 53px;
    border-top: 1.5px solid var(--ink);
    border-bottom: 1.5px solid var(--ink);
    display: flex;
    align-items: center;
    justify-content: center;
    font-family: 'Josefin Sans', 'Helvetica', sans-serif;
    font-weight: 300;
    font-size: 19px;
    letter-spacing: 4px;
    text-transform: uppercase;
  }
  .venue, .schedule {
    position: absolute;
    right: 25px;
    margin: 0;
    text-align: right;
    font-style: normal;
    font-size: 27px;
    letter-spacing: 3px;
    text-transform: uppercase;
    white-space: nowrap;
  }
  .venue { top: 178px; line-height: 39px; }
  .schedule { top: 506px; line-height: 39px; }
  .footnote {
    position: absolute;
    top: 680px;
    margin: 0;
    font-size: 22px;
    line-height: 1;
    letter-spacing: 3px;
    text-transform: uppercase;
    white-space: nowrap;
  }
  .footnote--gifts { left: 13px; }
  .footnote--host { right: 13px; }
</style>
</head>
<body>
<main class="invitation">
  <div class="art-slot art-slot--steins" style="left:45px" role="img" aria-label="Illustration of two beer steins clinking"></div>
  <div class="art-slot art-slot--steins" style="left:286px" role="img" aria-label="Illustration of two beer steins clinking"></div>
  <div class="art-slot art-slot--steins" style="left:527px" role="img" aria-label="Illustration of two beer steins clinking"></div>
  <div class="art-slot art-slot--steins" style="left:768px" role="img" aria-label="Illustration of two beer steins clinking"></div>
  <div class="art-slot art-slot--steins" style="left:1007px" role="img" aria-label="Illustration of two beer steins clinking"></div>
  <div class="rule rule--top"></div>

  <div class="photo-frame" role="img" aria-label="Space for a photo of Walt"></div>

  <p class="lead">It's not just a party... it's an</p>
  <h1 class="event-name">Oktoberfest</h1>
  <div class="celebrate"><span class="bars"></span><span>TO CELEBRATE</span><span class="bars"></span></div>
  <h2 class="honoree">Walt's 85<small>th</small> Birthday</h2>
  <div class="date">Saturday, October 25, 2014</div>

  <address class="venue">At the Thornwick Ale<br>Yard Pellorwood<br>4172 Dunmere Avenue<br>Hollin Vale, CA 93617</address>
  <p class="schedule">Cocktails at 6 Dinner at 7<br>Dancing &amp; Partying 'til 10</p>

  <p class="footnote footnote--gifts">No birthday gifts; please consider a gift to Pellorwood</p>
  <p class="footnote footnote--host">Hosted by Dora Penhale 555-318-0462</p>

  <div class="rule rule--bottom"></div>
  <div class="art-slot art-slot--hats" style="left:53px" role="img" aria-label="Illustration of a Bavarian felt hat"></div>
  <div class="art-slot art-slot--hats" style="left:301px" role="img" aria-label="Illustration of a Bavarian felt hat"></div>
  <div class="art-slot art-slot--hats" style="left:549px" role="img" aria-label="Illustration of a Bavarian felt hat"></div>
  <div class="art-slot art-slot--hats" style="left:797px" role="img" aria-label="Illustration of a Bavarian felt hat"></div>
  <div class="art-slot art-slot--hats" style="left:1045px" role="img" aria-label="Illustration of a Bavarian felt hat"></div>
</main>
</body>
</html>
```